Facebook post - Tidy Joint Crew has arrived to make your tiles smile!

Tidy Joint Crew would like to release a Facebook post calling out to the market that we have arrived. The company has a new and fresh branding aiming for a female demographic between the ages of 40 and 55 located in the South West of Western Australia. The company image MUST be centered around trust! Our Primary aim is to create an uncompromising trust from the very first impression. Our logo tag line is, 'We love to make your tiles smile'.
I need 5 x facebook template designs and also 5 x posts.
Our 1st campaign is to be 5 x posts centered around the arrival of this fantastic new company.
We are company that provides the services of:
- Grout and silicone repair.
- Broken or drummy tile replacement and;
- Grout sealing
Dont forget that we must communicate TRUST and the we love to make your tiles SMILE!

```html
<!DOCTYPE html>
<html lang="en">
<head>
<meta charset="utf-8">
<title>Tidy Joint Crew – Facebook Post</title>
<link rel="stylesheet" href="https://fonts.googleapis.com/css2?family=Bebas+Neue&family=Oswald:wght@300;400&family=Source+Sans+3:wght@400;600&display=swap">
<style>
  :root {
    --brand-blue: #2a9fd8;
    --deep-blue: #2a5f9e;
    --ink: #3d4148;
    --page: #eef1f5;
    --sky-top: #ffffff;
    --sky-mid: #e6f0f9;
    --water-pale: #dbe9f6;
    --water-light: #b9d4ee;
    --water-mid: #8db4de;
    --water-deep: #4f7fc0;
    --band: #d8e8f6;
    --rule: #2a9fd8;
  }
  * { box-sizing: border-box; margin: 0; padding: 0; }
  html, body { width: 746px; height: 1200px; overflow: hidden; }
  body { background: var(--page); position: relative; }

  .post {
    position: absolute; left: 23px; top: 250px;
    width: 700px; height: 700px;
    background: linear-gradient(180deg, var(--sky-top) 0%, var(--sky-mid) 70%);
    box-shadow: 0 3px 10px rgba(0,0,0,.18);
    overflow: hidden;
  }
  .headline {
    position: absolute; left: 52px; top: 34px; width: 596px;
    font-family: "Bebas Neue", sans-serif; font-size: 66px; line-height: 1;
    color: var(--brand-blue); letter-spacing: 1px; text-align: center;
  }
  .tagline {
    position: absolute; left: 52px; top: 100px; width: 596px;
    font-family: "Oswald", sans-serif; font-weight: 300; font-size: 24px; line-height: 30px;
    color: var(--ink); letter-spacing: 6px; text-align: center; white-space: nowrap;
  }
  .smile-word { position: relative; display: inline-block; }
  .smile-word svg {
    position: absolute; left: -4px; bottom: -12px; width: calc(100% + 6px); height: 14px;
  }
  .services-title {
    position: absolute; left: 52px; top: 159px; width: 596px; height: 42px;
    border: 2px solid var(--rule);
    font-family: "Source Sans 3", sans-serif; font-weight: 600; font-size: 24px;
    color: var(--brand-blue); text-align: center; line-height: 38px; white-space: nowrap;
  }
  .services {
    position: absolute; left: 54px; top: 218px; list-style: none;
    font-family: "Source Sans 3", sans-serif; font-size: 24px; color: var(--ink);
  }
  .services li { height: 45px; display: flex; align-items: center; gap: 6px; }
  .services svg { flex: none; }
  .reminder {
    position: absolute; left: 52px; top: 355px; width: 570px;
    font-family: "Source Sans 3", sans-serif; font-size: 20px; line-height: 26px; color: var(--ink);
  }
  .splash {
    position: absolute; left: 0; top: 420px; width: 700px; height: 215px;
    background:
      radial-gradient(ellipse 38% 45% at 68% 42%, rgba(79,127,192,.55), rgba(79,127,192,0) 75%),
      radial-gradient(ellipse 30% 22% at 25% 62%, rgba(42,95,158,.45), rgba(42,95,158,0) 80%),
      radial-gradient(ellipse 45% 35% at 88% 55%, rgba(42,95,158,.45), rgba(42,95,158,0) 80%),
      linear-gradient(180deg, rgba(219,233,246,0) 0%, var(--water-pale) 35%, var(--water-light) 60%, var(--water-mid) 100%);
  }
  .footer {
    position: absolute; left: 0; top: 635px; width: 700px; height: 65px;
    background: var(--band);
    display: flex; align-items: center; padding: 0 18px;
    font-family: "Source Sans 3", sans-serif; color: var(--ink);
  }
  .footer .divider { width: 2px; height: 34px; background: var(--rule); margin: 0 10px; }
  .brand { display: flex; align-items: center; gap: 7px; }
  .brand-dot { width: 14px; height: 14px; border-radius: 50%; background: var(--brand-blue); }
  .brand-name { font-size: 17px; font-weight: 600; color: var(--brand-blue); white-space: nowrap; }
  .contact { font-size: 10.5px; line-height: 14px; }
  .contact div { display: flex; align-items: center; gap: 4px; }
  .emergency { font-size: 11px; line-height: 13px; text-transform: uppercase; }
  .flood { display: flex; align-items: center; gap: 6px; font-size: 16px; text-transform: uppercase; white-space: nowrap; }
</style>
</head>
<body>
  <article class="post">
    <h1 class="headline">TIDY JOINT CREW</h1>
    <p class="tagline">WE LOVE TO MAKE “YOUR TILES <span class="smile-word">SMILE!”<svg viewBox="0 0 120 14" preserveAspectRatio="none"><path d="M2 3 Q60 18 118 2" fill="none" stroke="var(--brand-blue)" stroke-width="2.5" stroke-linecap="round"/></svg></span></p>

    <h2 class="services-title">WE ARE COMPANY THAT PROVIDES THE SERVICES OF</h2>
    <ul class="services">
      <li><svg width="20" height="18" viewBox="0 0 20 18"><path d="M2 10 L7 15 L18 2" fill="none" stroke="var(--ink)" stroke-width="2"/></svg>Grout and silicone repair.</li>
      <li><svg width="20" height="18" viewBox="0 0 20 18"><path d="M2 10 L7 15 L18 2" fill="none" stroke="var(--ink)" stroke-width="2"/></svg>Broken or drummy tile replacement and</li>
      <li><svg width="20" height="18" viewBox="0 0 20 18"><path d="M2 10 L7 15 L18 2" fill="none" stroke="var(--ink)" stroke-width="2"/></svg>Grout sealing</li>
    </ul>
    <p class="reminder">Dont forget that we must communicate TRUST and the we love to make your tiles SMILE!</p>

    <div class="splash" role="img" aria-label="Photograph of a clear blue water splash wave across the lower part of the post"></div>

    <footer class="footer">
      <div class="brand"><span class="brand-dot"></span><span class="brand-name">Tidy Joint Crew</span></div>
      <span class="divider"></span>
      <div class="contact">
        <div><svg width="9" height="9" viewBox="0 0 10 10"><circle cx="5" cy="5" r="5" fill="var(--brand-blue)"/><path d="M3 2.5 Q3 7 7.5 7" fill="none" stroke="#fff" stroke-width="1.3"/></svg>0491 570 118</div>
        <div><svg width="9" height="9" viewBox="0 0 10 10"><circle cx="5" cy="5" r="5" fill="var(--brand-blue)"/></svg>www.tidyjointcrew.com.au</div>
      </div>
      <span class="divider"></span>
      <div class="emergency">Emergency<br>Water Removal</div>
      <span class="divider"></span>
      <div class="flood">
        <svg width="30" height="30" viewBox="0 0 30 30"><circle cx="15" cy="15" r="13" fill="none" stroke="var(--brand-blue)" stroke-width="2.5"/><text x="15" y="19.5" text-anchor="middle" font-family="Oswald, sans-serif" font-size="12" fill="var(--brand-blue)">24</text></svg>
        Flood Response
      </div>
    </footer>
  </article>
</body>
</html>
```